Thornbury Lettings Managment Ltd website

Need a website To inform people/clients of the services we provide. 5 pages total with a local feel. Bristol, UK. I have logo artwork already is like the look based on
incorporate the artwork attached for theme, feel and colours fonts info etc

To best describe the business have a brief look at www.fernwickhomes.example.co.uk which is a local firm offering the same services. This is for your ref only and not to be copied.

Target Market(s)

Property Investors/Landlords

Coding

Coded - Design and coding required

Number of Pages Required

5+ page

Colors
0392cd
f68d4d

Requirements
Must have
• local feel. Possibly using some local architecture or historic landmarks etc. This is fexible.
• most also be mobile device compatible
Nice to have
• the membership logos - files attached: KTB, DWF, GMV and safehold-example.co.uk

```html
<!DOCTYPE html>
<html lang="en">
<head>
<meta charset="utf-8">
<title>Thornbury Lettings Managment Ltd</title>
<link href="https://fonts.googleapis.com/css2?family=Raleway:wght@400;500;600;700&display=swap" rel="stylesheet">
<style>
:root{
  --blue:#0392cd;
  --blue-dark:#2f7fa0;
  --orange:#f68d4d;
  --ink:#333;
  --muted:#555;
  --grey-bg:#efefef;
  --footer:#262626;
  --white:#fff;
}
*{box-sizing:border-box;margin:0;padding:0}
html,body{width:1200px;height:3025px;overflow:hidden}
body{font-family:'Raleway',sans-serif;color:var(--ink);background:var(--white);position:relative}
.topbar{height:20px;background:var(--blue);display:flex;justify-content:space-between;align-items:center;padding:0 100px;color:var(--white);font-size:11px}
.socials{display:flex;gap:4px}
.socials span{width:18px;height:16px;background:rgba(255,255,255,.25)}
.header{height:95px;display:flex;align-items:center;justify-content:space-between;padding:0 100px 0 100px}
.brand{display:flex;align-items:center;gap:12px}
.brand-square{width:48px;height:48px;background:var(--blue-dark)}
.brand-name{font-size:26px;font-weight:700;color:var(--blue-dark);line-height:1}
.brand-sub{font-size:13px;font-weight:700;color:var(--blue-dark)}
.nav{display:flex;gap:48px;font-size:15px;font-weight:500;color:#222}
.hero{height:555px;background:linear-gradient(180deg,#6b6b6b,#3c3c3c 55%,#2a2a2a);position:relative}
.hero-panel{position:absolute;left:302px;top:137px;width:590px;height:283px;background:rgba(246,141,77,.82);border:2px solid rgba(255,255,255,.6);outline:8px solid rgba(246,141,77,.82);text-align:center;color:var(--white);padding-top:34px}
.hero-mark{width:64px;height:64px;background:var(--white);margin:0 auto 22px;border-radius:50%}
.hero-title{font-size:28px;font-weight:700;letter-spacing:1px}
.hero-text{font-size:14px;line-height:22px;width:480px;margin:14px auto 0}
.dots{display:flex;justify-content:center;gap:18px;margin-top:26px}
.dots span{width:8px;height:8px;border-radius:50%;background:var(--white)}
.section-head{display:flex;justify-content:center;align-items:center;gap:12px}
.section-head .mark{width:44px;height:44px;background:var(--blue-dark)}
.section-head .title{font-size:20px;font-weight:600;color:#222;border-left:1px solid #aaa;padding-left:10px}
.section-head .sub{font-size:13px;color:var(--muted)}
.intro{height:322px;padding-top:42px;text-align:center}
.intro p{width:1100px;margin:28px auto 0;font-size:13px;line-height:20px;color:#333}
.btns{display:flex;justify-content:center;gap:22px;margin-top:22px}
.btn{display:inline-block;padding:8px 22px;font-size:13px;color:var(--white);border-radius:3px}
.btn-blue{background:var(--blue-dark)}
.btn-orange{background:var(--orange)}
.feature{display:flex;height:341px}
.feature .photo{width:600px;height:341px}
.feature .copy{width:600px;padding:54px 40px 0 30px;color:var(--white)}
.copy.orange{background:var(--orange)}
.copy.blue{background:var(--blue)}
.copy.left{padding-left:100px}
.copy h3{display:flex;align-items:center;gap:12px;font-size:20px;font-weight:600}
.copy h3 span{width:22px;height:22px;background:var(--white)}
.copy .lead{font-size:14px;font-weight:700;line-height:21px;margin-top:22px}
.copy .body{font-size:12px;line-height:21px;margin-top:12px;opacity:.9}
.btn-ghost{display:inline-block;margin-top:20px;border:1px solid var(--white);border-radius:3px;padding:6px 16px;font-size:12px}
.services{height:546px;background:var(--grey-bg);padding-top:30px}
.cards{display:flex;justify-content:space-between;width:1000px;margin:42px auto 0}
.card{width:312px;height:399px;background:var(--white);position:relative}
.card-head{height:50px;display:flex;align-items:center;color:var(--white);font-size:15px;font-weight:500;background:var(--blue)}
.card-head .tab{width:60px;height:50px;background:var(--orange);clip-path:polygon(0 0,100% 0,70% 100%,0 100%);margin-right:10px}
.card-head.orange{background:var(--orange)}
.card-head.orange .tab{background:var(--blue)}
.card .photo{height:194px}
.card p{font-size:13px;line-height:21px;padding:18px 14px 0;color:#333}
.card .btn{position:absolute;left:12px;bottom:22px;background:var(--blue-dark)}
.partners{height:146px;display:flex;align-items:center;justify-content:space-between;padding:0 100px}
.arrow{width:20px;height:30px}
.badges{display:flex;align-items:center;gap:100px}
.badge-wide{font-size:30px;font-weight:600;color:var(--blue)}
.badge{width:60px;height:56px;border-radius:4px}
.footer{height:268px;background:var(--footer);color:#ddd;display:flex;padding:56px 100px 0;font-size:13px}
.footer h4{font-size:14px;font-weight:600;color:var(--white);margin-bottom:24px;letter-spacing:.5px}
.col-contact{width:330px}
.col-links{width:180px}
.col-community{width:240px}
.col-news{width:250px}
.contact-row{display:flex;gap:16px;line-height:24px;margin-bottom:4px}
.contact-row svg{flex:none;margin-top:6px}
.col-links li{list-style:none;line-height:24px}
.community-name{display:flex;align-items:center;gap:8px;font-size:20px;font-weight:700;color:var(--white);margin-bottom:12px}
.community-name span{width:40px;height:40px;background:var(--white)}
.col-community p{line-height:20px}
.field{margin-top:20px;height:32px;border:1px solid #555;background:#1d1d1d;padding:7px 10px;font-size:12px;color:#ccc}
.signup{margin-top:8px;height:34px;background:var(--blue);color:var(--white);text-align:center;font-size:13px;font-weight:600;line-height:34px}
.bottombar{height:50px;background:var(--blue);color:var(--white);display:flex;justify-content:space-between;align-items:center;padding:0 100px;font-size:12px}
.circles{display:flex;gap:14px}
.circles span{width:26px;height:26px;border:1px solid var(--white);border-radius:50%}
</style>
</head>
<body>
<div class="topbar">
  <div class="socials"><span></span><span></span><span></span><span></span></div>
  <div>Email:hello@thornburylettings.example</div>
</div>

<header class="header">
  <div class="brand">
    <div class="brand-square"></div>
    <div><div class="brand-name">Thornbury</div><div class="brand-sub">lettings managment ltd</div></div>
  </div>
  <nav class="nav"><span>Home</span><span>About</span><span>Commercial</span><span>Landlords</span><span>Contact</span><span>Blog</span></nav>
</header>

<section class="hero" role="img" aria-label="Black and white photograph of historic Bristol rooftops and a cathedral tower">
  <div class="hero-panel">
    <div class="hero-mark"></div>
    <div class="hero-title">THORNBURYLETTINGS</div>
    <p class="hero-text">Thornbury Lettings is an independent Estate Agent and Letting Agent in Bristol, Redland. We cover most areas in Bristol and surrounding areas.</p>
    <div class="dots"><span></span><span></span><span></span></div>
  </div>
</section>

<section class="intro">
  <div class="section-head"><div class="mark"></div><div><div class="title">Thornbury Lettings</div><div class="sub title" style="font-size:13px;font-weight:400;color:#555">Bristol based independent</div></div></div>
  <p>Thornbury Lettings is an independent Estate Agent and Letting Agent in Bristol, Redland. We cover most areas in Bristol and surrounding areas, our offices are open 7 Days a Week and we can arrange viewings at flexible times Monday - Sunday. Please click on the relevant pages for more information for Tenants and Landlords. Whether you are a landlord or a tenant, make Thornbury Lettings your first choice to help with your Lettings and Sales needs. Find all the services and guidance we offer to Landlords to help you let your property. We can help tenants find the ideal new home and make moving a joy not a hassle. Click here for our Commercial Estate Agents.</p>
  <div class="btns"><span class="btn btn-blue">Read More</span><span class="btn btn-orange">Contact Us</span></div>
</section>

<section class="feature">
  <div class="photo" role="img" aria-label="Photograph of red brick riverside apartments under a blue sky" style="background:linear-gradient(180deg,#8fb8e0,#b46a4a 50%,#6f8fa0)"></div>
  <div class="copy orange">
    <h3><span></span>FOR LANDLORDS</h3>
    <p class="lead">We have many years experience in the property industry including developments and property management</p>
    <p class="body">We offer landlords and tenants a professional and complete service including let only and fully managed options, we can take the stress out of letting your property whether you have 1 or 100 we can provide a one stop solution. We use reputable reference agency to ensure tenants are reliable and your investment is protected.</p>
    <span class="btn-ghost">Read More</span>
  </div>
</section>
<section class="feature">
  <div class="copy blue left">
    <h3><span></span>FOR TENANTS</h3>
    <p class="lead">We have many years experience in the property industry including developments and property management</p>
    <p class="body">We offer landlords and tenants a professional and complete service including let only and fully managed options, we can take the stress out of letting your property whether you have 1 or 100 we can provide a one stop solution. We use reputable reference agency to ensure tenants are reliable and your investment is protected.</p>
    <span class="btn-ghost">Read More</span>
  </div>
  <div class="photo" role="img" aria-label="Photograph of a suburban brick semi-detached house with hedges" style="background:linear-gradient(180deg,#a9c4dc,#9a6e58 55%,#4f6b3a)"></div>
</section>
<section class="feature">
  <div class="photo" role="img" aria-label="Photograph of a modern apartment block with round balconies" style="background:linear-gradient(180deg,#7ea9d6,#a55a3e 55%,#8a8a8a)"></div>
  <div class="copy orange">
    <h3><span></span>FOR AGENCIES</h3>
    <p class="lead">We have many years experience in the property industry including developments and property management</p>
    <p class="body">We offer landlords and tenants a professional and complete service including let only and fully managed options, we can take the stress out of letting your property whether you have 1 or 100 we can provide a one stop solution. We use reputable reference agency to ensure tenants are reliable and your investment is protected.</p>
    <span class="btn-ghost">Read More</span>
  </div>
</section>

<section class="services">
  <div class="section-head"><div class="mark"></div><div><div class="title">Thornbury Services</div><div class="title" style="font-size:13px;font-weight:400;color:#555">Bristol based independent</div></div></div>
  <div class="cards">
    <article class="card">
      <div class="card-head"><span class="tab"></span>FEATURED PROPERTIES</div>
      <div class="photo" role="img" aria-label="Photograph of a family home with a lawn" style="background:linear-gradient(180deg,#9cc4e6,#9a7a5a 55%,#5d8a3a)"></div>
      <p>At Thornbury Lettings, we offer our clients a high quality value for money lettings service. We are a well established lettings agent</p>
      <span class="btn">Read More</span>
    </article>
    <article class="card">
      <div class="card-head orange"><span class="tab"></span>NEW ARRIVALS</div>
      <div class="photo" role="img" aria-label="Photograph of a newly built detached house" style="background:linear-gradient(180deg,#7fb0e0,#c9c2b6 55%,#6a7a58)"></div>
      <p>We offer landlords and tenants a professional and complete service including let only and fully managed options, we can take the stress out</p>
      <span class="btn">Read More</span>
    </article>
    <article class="card">
      <div class="card-head"><span class="tab"></span>ON SALE PROPERTIES</div>
      <div class="photo" role="img" aria-label="Photograph of a city skyline with tall towers" style="background:linear-gradient(180deg,#bcd6ee,#8a98a8 60%,#4f5a66)"></div>
      <p>Thinking of selling your property? We understand that selling your property can sometimes be a daunting process but with over 20 years</p>
      <span class="btn">Read More</span>
    </article>
  </div>
</section>

<section class="partners">
  <svg class="arrow" viewBox="0 0 20 30"><path d="M15 3 L4 15 L15 27" fill="none" stroke="#222" stroke-width="3"/></svg>
  <div class="badges">
    <span class="badge-wide">safehold-example.co.uk</span>
    <span class="badge" style="background:#2a8fbf" aria-label="KTB membership badge"></span>
    <span class="badge" style="background:#7b4a9e;width:90px" aria-label="GMV membership badge"></span>
    <span class="badge" style="background:#a32222" aria-label="DWF membership badge"></span>
  </div>
  <svg class="arrow" viewBox="0 0 20 30"><path d="M5 3 L16 15 L5 27" fill="none" stroke="#222" stroke-width="3"/></svg>
</section>

<footer class="footer">
  <div class="col-contact">
    <h4>CONTACT US</h4>
    <div class="contact-row"><svg width="10" height="13" viewBox="0 0 10 13"><path d="M5 0a5 5 0 0 0-5 5c0 4 5 8 5 8s5-4 5-8a5 5 0 0 0-5-5z" fill="#fff"/><circle cx="5" cy="5" r="2" fill="#262626"/></svg><span>Thornbury Lettings 14 Kestrel Row<br>Redland, Bristol</span></div>
    <div class="contact-row"><svg width="12" height="9" viewBox="0 0 12 9"><rect width="12" height="9" fill="#fff"/><path d="M0 0l6 5 6-5" fill="none" stroke="#262626"/></svg><span>Email: office@thornburylettings.example</span></div>
    <div class="contact-row"><svg width="12" height="12" viewBox="0 0 12 12"><path d="M2 0h3l1 3-2 1.5a7 7 0 0 0 3.5 3.5L9 6l3 1v3a2 2 0 0 1-2 2A10 10 0 0 1 0 2a2 2 0 0 1 2-2z" fill="#fff"/></svg><span>Phone: +44 (0) 117 000 0000</span></div>
  </div>
  <div class="col-links">
    <h4>QUICK LINKS</h4>
    <ul><li>Home</li><li>About Us</li><li>Commercial</li><li>Blog</li><li>Contact Us</li></ul>
  </div>
  <div class="col-community">
    <h4>OUR COMMUNITY</h4>
    <div class="community-name"><span></span>Thornbury</div>
    <p>Informationsabende 2016<br>Mittagstisch / Speiseplan<br>Abschlussprüfungen</p>
  </div>
  <div class="col-news">
    <h4>NEWSLETTER</h4>
    <p style="line-height:18px">Lorem ipsum dolor sit amet, consectetur adipisicing elit dignissimos.</p>
    <div class="field">Email</div>
    <div class="signup">SIGN UP NOW</div>
  </div>
</footer>
<div class="bottombar">
  <span>© 2016 Thornbury Lettings. All Rights Reserved</span>
  <div class="circles"><span></span><span></span><span></span><span></span></div>
</div>
</body>
</html>
```